Bright Years Forward an age management group needs a modern looking website developed asap

Bright Years Forward is an age management group lead by a board certified medical doctor (who also specializes in age management medicine) and a 7th degree black belt jiu-jitsu master. Both have joined forces to create a unique doctor supervised anti-aging medical, nutritional, hormonal, exercise protocol never seen before.
This marriage between medicine and athleticism will create the worlds first complete anti-aging program designed for anyone wishing to remain as healthy and as young for as long as possible.

Our Mission and Vision: "To provide clients cutting edge anti aging programs and protocols designed to "turn-back-the-clock-one-second-at-a-time. Let's all Bright Years Forward..together!"

Bright Years Forward's program consists of 6 unique tiers/platforms each encompassing a specific need.
The 6 tiers are:
1. Apex Care: A medical doctor supervised unique and proprietary hormone optimization program and protocol developed by a board certified medical doctor trained by Volarix ( a world leader in age management medicine) who has practiced age management medicine for the past 7 years
2. Apex Slim: A medical doctor supervised unique and proprietary weight management program and protocol developed by a published medical doctor who's diet book "Fresh start: Shed those pounds soon" was just launched
3.Apex Motion: A master athlete supervised training program and protocol, with access to a large proprietary exercise video databank developed by a 7th degree black belt jiu-jitsu master.
4. Apex Plate: A chef driven and supervised home delivered healthy meals. Each meal is made from scratch, and is specifically tailored and targeted according to each patient's specific needs.
5. ApexDailyMix: A doctor formulated-master athlete approved most complete multi vitamin-mineral-anti-oxidant and supplement pack available on the market today. ApexDailyMix is: made in the USA, and QSA approved vitamin factory, gluten free, sugar free, and artificial color free.
6. Apex Academy: A unique CME approved teaching workshop intended for those physicians who lack expertise in age management but want to become proficient in the art of hormone optimization and age management medicine. The 2-day workshop is held twice monthly on Saturday and Sunday in sunny Florida.

This is our scope and goal.
We want to become the leaders in age management medicine by being the first to unite doctors-athletes-chefs-nutritionist together in an effort to deliver the most advanced most cutting edge programs and protocols so we may all : BRIGHT YAERS FORWARD!

We already have the logo for Bright years forward.
Please keep in mind the following:
1. Apex care should be in green and black
2. Apex slim should be in purple and black
3. Apex motion in orange and black
4. Apx plate in yellow and black
5. ApexDialyMix in red and black
6. Apex academy in gray and black

Target Market(s)

Adults Males and females wishing to remain as healthy and as young for as long as possible
Obese and overweight adults males and females
Athletes males and females
Young obese and overweight males and females
ALL can be from any country!

Industry/Entity Type

Health And Wellness

Coding

Coded - Design and coding required

Number of Pages Required

5+ page

Requirements
Must have
• The front page must have our mission statement as well as the 6 tiers/platforms displayed (Apex Care, Apex Slim, Apex Motion, Apex Plate, ApexDailyMix, Apex Academy) and each platform when "cliked on" should open up in its own unique page.
• The capability for clients to log on to any of the pages using assigned usernames and passwords.
• The capability of check out (credit cards, paypal) from any of the pages. EX the client may want to buy ApexDailyMix. He/She would click on the main page then click on ApexDailymix page and choose to buy the vitamin. Same For the rest: He/she may want to buy the weight loss program (apex slim), or the Hormone program (apex care) or the food delivered home (apex Plate) or apex motion (access to the exercise video databank) or attend the workshop (buy the teaching program..BUT this will ONLY be accessible if the client is a medical doctor and has a valid medical license).
• Also the client may want to have full access to ALL the 6 tiers, thus on the FRONT page we need a checkout with "full access to tiers"
• Also we need to make sure no videos are downloade but only viewed. we need to have this safety built in.
• Also we nee to be able to keep track of emails and have stats. and any email inquiry must be diverted to my iphone.
Nice to have
• Modern look with pop-ups and graphics and iphone and android capability
Should not have
• nothing explicit

```html
<!DOCTYPE html>
<html lang="en">
<head>
<meta charset="utf-8">
<title>Bright Years Forward</title>
<link rel="stylesheet" href="https://fonts.googleapis.com/css2?family=Roboto:wght@300;400;500;700&family=Yellowtail&family=Play:wght@700&display=swap">
<style>
:root{
  --ink:#222;
  --muted:#777;
  --black:#0b0b0b;
  --white:#fff;
  --bar:#e6e6e6;
  --soft:#f4f5f7;
  --blue:#3b8ff0;
  --green:#0b8a12;
  --purple:#83108a;
  --orange:#f6a208;
  --yellow:#c8cf0a;
  --red:#ee0c0c;
  --gray:#7b7b7b;
  --cream:#f4efe4;
}
*{box-sizing:border-box;margin:0;padding:0}
html,body{width:1200px;height:2582px;overflow:hidden}
body{position:relative;font-family:"Roboto",Arial,sans-serif;color:var(--ink);background:var(--white)}
.abs{position:absolute}

/* top bar */
.brand-bar{left:0;top:0;width:1200px;height:45px;background:var(--bar);display:flex;align-items:center;justify-content:center}
.brand-name{font-size:26px;font-weight:700;color:#2a2a2a;letter-spacing:.5px}

/* hero */
.hero{left:0;top:45px;width:1200px;height:549px;overflow:hidden;
  background:
    radial-gradient(ellipse 420px 260px at 180px 150px,rgba(255,236,170,.75),rgba(255,236,170,0) 70%),
    linear-gradient(180deg,#56606c 0%,#8e8a74 22%,#c9a95a 45%,#a47b3a 62%,#6e4f2a 80%,#3a2a18 100%)}
.nav{position:absolute;top:22px;left:0;width:1200px;height:34px}
.nav a{position:absolute;top:8px;color:var(--white);font-size:15px;text-decoration:none;transform:translateX(-50%);white-space:nowrap}
.nav .login{top:0;background:#000;border-radius:6px;padding:8px 14px;transform:none}
.hero-title{position:absolute;left:430px;top:178px;width:640px;height:84px;text-align:center;font-family:"Yellowtail",cursive;font-size:74px;color:var(--white);line-height:84px;white-space:nowrap;overflow:visible}
.hero-sub{position:absolute;left:500px;top:268px;width:480px;text-align:center;color:var(--white);font-size:21px;font-weight:500;white-space:nowrap}
.btn{position:absolute;top:324px;height:36px;font-size:10px;font-weight:700;display:flex;align-items:center;justify-content:center;color:var(--white);border-radius:3px;letter-spacing:.3px;white-space:nowrap}
.btn-buy{left:623px;width:128px;background:var(--blue)}
.btn-surf{left:759px;width:107px;border:1.5px solid rgba(255,255,255,.9)}

/* stats */
.stats{left:0;top:594px;width:1200px;height:172px;background:var(--white)}
.stat{position:absolute;top:10px;width:300px;text-align:center;transform:translateX(-50%)}
.stat-label{font-size:19px;font-weight:300;color:#333}
.stat-num{font-size:43px;font-weight:700;color:#2a2a2a;margin-top:12px}
.stats-rule{position:absolute;left:66px;top:134px;width:1070px;height:1px;background:#ddd}
.like-box{position:absolute;left:375px;top:112px;width:450px;height:44px;border:1px solid #ddd;border-radius:22px;background:var(--white);display:flex;align-items:center}
.like-thumb{width:60px;height:44px;border-right:1px solid #e4e4e4;display:flex;align-items:center;justify-content:center}
.like-btn{margin-left:36px;background:#4a6ec2;color:var(--white);font-size:10px;font-weight:700;padding:3px 6px;border-radius:2px;display:flex;align-items:center;gap:3px}
.like-text{margin-left:6px;font-size:10px;color:#333}

/* wellness */
.wellness{left:0;top:766px;width:1200px;height:358px;background:var(--soft)}
.section-title{position:absolute;left:0;width:1200px;text-align:center;font-size:21px;font-weight:500;color:#222}
.dots{position:absolute;left:52px;width:1096px;border-top:1.5px dotted #c9c9c9}
.pillar{position:absolute;top:106px;width:360px;transform:translateX(-50%);text-align:center}
.pillar-icon{width:75px;height:80px;background:#000;margin:0 auto;display:flex;align-items:center;justify-content:center}
.pillar h3{font-size:18px;font-weight:500;margin-top:20px;color:#222}
.pillar p{font-size:12.5px;line-height:1.6;color:var(--muted);margin-top:14px}

/* parallax */
.parallax{left:0;top:1124px;width:1200px;height:276px;
  background:
    radial-gradient(ellipse 360px 150px at 960px 170px,rgba(255,255,180,.95),rgba(240,240,90,.5) 40%,rgba(240,240,90,0) 75%),
    linear-gradient(180deg,#3d5f92 0%,#6d89a8 35%,#c9c67a 62%,#a7b62a 78%,#5f7a12 100%)}
.parallax-text{position:absolute;left:0;top:10px;font-family:"Play",sans-serif;font-weight:700;font-size:40px;line-height:53px;color:var(--white);white-space:nowrap}

/* programs */
.card{position:absolute;width:347px;height:250px;background:var(--black);border-radius:4px;text-align:center;color:var(--white);padding:68px 20px 0}
.card-badge{position:absolute;left:50%;top:-47px;width:94px;height:94px;border-radius:50%;transform:translateX(-50%)}
.card h3{font-size:18px;font-weight:700;margin-top:0}
.card p{font-size:12.5px;line-height:1.55;margin-top:16px;color:var(--cream)}
.tier-care .card-badge{background:var(--green)}
.tier-slim .card-badge{background:var(--purple)}
.tier-motion .card-badge{background:var(--orange)}
.tier-plate .card-badge{background:var(--yellow)}
.tier-mix .card-badge{background:var(--red)}
.tier-academy .card-badge{background:var(--gray)}

/* footer */
.footer{left:0;top:2166px;width:1200px;height:416px;background:#000;color:var(--white)}
.fcol{position:absolute;top:48px;width:250px}
.fcol h4{font-size:18px;font-weight:700;margin-bottom:22px}
.fcol p{font-size:12.5px;line-height:1.6;margin-bottom:16px}
.social{display:flex;gap:12px;margin-top:-2px}
.social span{width:12px;height:12px;border-radius:50%;background:var(--white)}
.post{display:flex;gap:16px;margin-bottom:22px;align-items:flex-start}
.thumb{flex:none;width:46px;height:46px;border-radius:50%;background:#c9c9c9;color:#555;font-size:8px;display:flex;align-items:center;justify-content:center;margin-top:4px}
.post-title{font-size:12.5px}
.post-meta{font-size:10.5px;color:#ccc;margin-top:6px}
.quote{display:flex;gap:10px}
.quote-mark{font-family:Georgia,serif;font-size:64px;line-height:.8;color:#9a9a9a;font-weight:700}
.quote p{font-size:12.5px;line-height:1.6;color:var(--cream)}
.reviewer{display:flex;align-items:center;gap:16px;margin-top:14px}
.avatar{width:78px;height:78px;border-radius:50%;background:#c9c9c9;color:#333;font-size:13px;display:flex;align-items:center;justify-content:center}
.reviewer-name{font-size:16px;color:var(--cream)}
.reviewer-role{font-size:12.5px;margin-top:8px}
.footer-rule{position:absolute;left:52px;top:350px;width:1096px;height:1px;background:#333}
.copyright{position:absolute;left:0;top:376px;width:1200px;text-align:center;font-size:12.5px}
</style>
</head>
<body>

<header class="abs brand-bar"><span class="brand-name">Bright Years Forward</span></header>

<section class="abs hero" role="img" aria-label="Runner's legs in trail shoes on a sunlit grassy hillside">
  <nav class="nav">
    <a style="left:237px">Apex care</a>
    <a style="left:377px">Apex slim</a>
    <a style="left:500px">Apex motion</a>
    <a style="left:608px">Apx plate</a>
    <a style="left:741px">ApexDialyMix</a>
    <a style="left:880px">Apex academy</a>
    <a class="login" style="left:962px">Login</a>
  </nav>
  <div class="hero-title">Ready to Enjoy?</div>
  <div class="hero-sub">Grab This Perfect Team Now!</div>
  <div class="btn btn-buy">I LIKE IT! PURCHASE</div>
  <div class="btn btn-surf">GO ON SURFING</div>
</section>

<section class="abs stats">
  <div class="stat" style="left:224px"><div class="stat-label">Days Worked</div><div class="stat-num">640 +</div></div>
  <div class="stat" style="left:599px"><div class="stat-label">Satisfied Clients</div><div class="stat-num">100 +</div></div>
  <div class="stat" style="left:975px"><div class="stat-label">Specialists</div><div class="stat-num">50 +</div></div>
  <div class="stats-rule"></div>
  <div class="like-box">
    <div class="like-thumb"><svg width="18" height="18" viewBox="0 0 18 18" fill="none" stroke="#bbb" stroke-width="1.4"><rect x="2" y="8" width="3" height="8"/><path d="M5 8l4-6c1.5 0 2 1 1.6 2.5L10 7h5c1 0 1.5 1 1.2 2l-1.5 6c-.2.7-.8 1-1.5 1H5"/></svg></div>
    <span class="like-btn"><svg width="9" height="8" viewBox="0 0 9 8"><path d="M1 4l2.5 2.5L8 1" stroke="#fff" stroke-width="1.6" fill="none"/></svg>Like</span>
    <span class="like-text">You and 4.1k others like this.</span>
  </div>
</section>

<section class="abs wellness">
  <h2 class="section-title" style="top:26px">Health And Wellness</h2>
  <div class="dots" style="top:64px"></div>
  <div class="pillar" style="left:224px">
    <div class="pillar-icon"><svg width="44" height="44" viewBox="0 0 44 44" fill="none" stroke="#fff" stroke-width="2"><rect x="5" y="20" width="8" height="18"/><path d="M13 21l8-12c3 0 4 2 3 5l-2 6h12c2 0 3.5 2 3 4l-3 11c-.4 1.5-1.6 2-3 2H13"/></svg></div>
    <h3>Who we are</h3>
    <p>Bright Years Forward is an age management group lead by a board certified medical doctor (who also specializes in age management medicine) and a 7th degree black belt jiu-jitsu master</p>
  </div>
  <div class="pillar" style="left:599px">
    <div class="pillar-icon"><svg width="40" height="44" viewBox="0 0 40 44" fill="none" stroke="#fff" stroke-width="2"><path d="M20 4c6 6 7 15 5 24H15c-2-9-1-18 5-24z"/><circle cx="20" cy="17" r="3"/><path d="M15 24l-5 6v4l5-3M25 24l5 6v4l-5-3M17 32l3 7 3-7"/></svg></div>
    <h3>Our Mission</h3>
    <p>To provide clients cutting edge anti aging programs and protocols designed to "turn-back-the-clock-one-second-at-a-time. Let's all Bright Years Forward..together!</p>
  </div>
  <div class="pillar" style="left:975px">
    <div class="pillar-icon"><svg width="36" height="44" viewBox="0 0 36 44" fill="none" stroke="#fff" stroke-width="2"><path d="M5 3h18l8 8v30H5z"/><path d="M23 3v8h8M11 20h14M11 26h14M11 32h14"/></svg></div>
    <h3>Our Vision</h3>
    <p>To provide clients cutting edge anti aging programs and protocols designed to "turn-back-the-clock-one-second-at-a-time. Let's all Bright Years Forward..together!</p>
  </div>
</section>

<section class="abs parallax" role="img" aria-label="Sun setting over a green meadow under a wide sky">
  <div class="parallax-text">Parallax Images<br>&nbsp;Move on scroll</div>
</section>

<section class="abs" style="left:0;top:1400px;width:1200px;height:766px">
  <h2 class="section-title" style="top:18px">Bright Years Forward's Program Consists</h2>
  <div class="dots" style="top:57px"></div>

  <article class="card tier-care" style="left:52px;top:126px">
    <div class="card-badge" role="img" aria-label="Figure in a balanced yoga pose"></div>
    <h3>Apex care</h3>
    <p>A medical doctor supervised unique and proprietary hormone optimization program and protocol developed by a board certified medical doctor trained by Volarix ( a world leader in age management medicine) who has practiced age management medicine for the past 7 years</p>
  </article>
  <article class="card tier-slim" style="left:426px;top:126px">
    <div class="card-badge" role="img" aria-label="Figure stretching one arm overhead"></div>
    <h3>Apex slim</h3>
    <p>A medical doctor supervised unique and proprietary weight management program and protocol developed by a published medical doctor who's diet book "Fresh start: Shed those pounds soon" was just launched</p>
  </article>
  <article class="card tier-motion" style="left:801px;top:126px">
    <div class="card-badge" role="img" aria-label="Figure in an athletic stance"></div>
    <h3>Apex motion</h3>
    <p>A master athlete supervised training program and protocol, with access to a large proprietary exercise video databank developed by a 7th degree black belt jiu-jitsu master</p>
  </article>

  <article class="card tier-plate" style="left:52px;top:494px">
    <div class="card-badge" role="img" aria-label="Figure with arms raised in a star jump"></div>
    <h3>Apx plate</h3>
    <p>A chef driven and supervised home delivered healthy meals. Each meal is made from scratch, and is specifically tailored and targeted according to each patient's specific needs</p>
  </article>
  <article class="card tier-mix" style="left:423px;top:494px">
    <div class="card-badge" role="img" aria-label="Figure in a seated forward stretch"></div>
    <h3>Apex DialyMix</h3>
    <p>A doctor formulated-master athlete approved most complete multi vitamin-mineral-anti-oxidant and supplement pack available on the market today. ApexDailyMix is: made in the USA, and QSA approved vitamin factory, gluten free, sugar free, and artificial color free.</p>
  </article>
  <article class="card tier-academy" style="left:794px;top:494px">
    <div class="card-badge" role="img" aria-label="Figure seated in a side stretch"></div>
    <h3>Apex academy</h3>
    <p>A unique CME approved teaching workshop intended for those physicians who lack expertise in age management but want to become proficient in the art of hormone optimization and age management medicine. The 2-day workshop is held twice monthly on Saturday and Sunday in sunny Florida</p>
  </article>
</section>

<footer class="abs footer">
  <div class="fcol" style="left:52px">
    <h4>Contact Us</h4>
    <p>Maecenas etos sit amet, consectetur adipiscing elit. Terminal volutpat rutrum metro amet sollicitudin interdum.</p>
    <p>Phone: +1 (800) 555 01 48</p>
    <p>Office: 4710 Linden Avenue, New York</p>
    <p>Email: hello@brightyearsforward.com</p>
    <div class="social"><span></span><span></span><span></span><span></span><span></span></div>
  </div>
  <div class="fcol" style="left:332px">
    <h4>Recent Posts</h4>
    <div class="post"><div class="thumb">50x50</div><div><div class="post-title">Business Cards Design Trends</div><div class="post-meta">Dec 02, 2020 / 2 comments</div></div></div>
    <div class="post"><div class="thumb">50x50</div><div><div class="post-title">This Maravelous App</div><div class="post-meta">Nov 18, 2020 / 9 comments</div></div></div>
    <div class="post"><div class="thumb">50x50</div><div><div class="post-title">Brand Paper Niceties</div><div class="post-meta">Nov 10, 2020 / 0 comments</div></div></div>
  </div>
  <div class="fcol" style="left:615px">
    <h4>Latest Twitts</h4>
  </div>
  <div class="fcol" style="left:895px">
    <h4>Last Review</h4>
    <div class="quote"><span class="quote-mark">&ldquo;</span><p>Lorem ipsum dolor sit amet, consectetur adipiscing elit, sed do eiusmod tempor incididunt ut labore et dolore magna aliqua. Ut enim ad minim veniam, quis nostrud exercitation ullamco.</p></div>
    <div class="reviewer"><div class="avatar">84x84</div><div><div class="reviewer-name">Nolan Avery</div><div class="reviewer-role">Creative Designer</div></div></div>
  </div>
  <div class="footer-rule"></div>
  <div class="copyright">Copyright 2020. All Rights Reserved by Bright Years Forward's</div>
</footer>

</body>
</html>
```